依頼詳細
・当社で建築した物件とイメージキャラクターをデザインに盛り込んだ提案をお願いします。(添付ファイル有)
・封筒の色は白で考えています。
・封筒サイズ:角2、角0(角2と同じデザイン)、長3(縦向き)
記載項目
・会社ロゴ ・会社マーク ※添付ファイル有
〒245-0623
神奈川県横浜市戸塚区下柏尾町517-4 リベルタ北園3F
TEL 045-770-2914(代表)
045-770-2957(工事部)
045-770-2986(不動産部)
FAX 045-770-2938
www.hinorisa-corp.com
E-mail info@hinorisa-corp.com
・当社で建築した物件(添付ファイル写真)のいずれかを背景等に使って下さい。
・イメージキャラクター ヒノリくん(添付ファイル有)
希望イメージ
• +5 0 +5
• シンプル
複雑
• 単色
カラフル
• 暗い
明るい
• 日常
高級
• 遊び心
厳粛
• 未来的
伝統的
• 女性的
男性的
希望する色
緑系、黄・オレンジ系、物件写真はモノクロやセピア調に加工して頂いてもかまいません。
納品ファイル
• 高解像度JPG (.jpg)
補足説明
当社の名刺も添付します。
3段目、4段目のような雰囲気をイメージして頂くといいかと思います。
依頼公開後の追記内容
■ 選んだ理由

色使いや配置が細部にわたりバランス良く、綺麗にまとまっていました。
重要な書類の送付にも問題なく、また社員投票でも一番人気だったので選ばせて頂きました。

■ 提案者全員のお礼・コメント

ランサーの皆さま、この度は当社の会社封筒デザインにたくさんの素敵なご提案を頂きましてありがとうございます。

皆さまの作品のコメントを拝見すると、どれも「なるほど!」と思うものばかりで、一点を選ぶのに大変苦労しました。

また何かご縁がありました際にはよろしくお願い致します。

```html
<!DOCTYPE html>
<html lang="ja">
<head>
<meta charset="utf-8">
<title>ヒノリサコーポレーション 封筒デザイン</title>
<link rel="stylesheet" href="https://fonts.googleapis.com/css2?family=Noto+Sans+JP:wght@400;700;900&display=swap">
<style>
  :root {
    --paper: #ffffff;
    --ink: #2a2a2a;
    --brand-red: #c8261e;
    --band-brown: #7a5a32;
    --band-text: #f3d44a;
    --branch: #9a9a9a;
    --wash-top: rgba(255,255,255,0);
    --wash-warm: #e9dcc6;
    --wash-deep: #cdb894;
    --frame: #ffffff;
  }
  * { margin: 0; padding: 0; box-sizing: border-box; }
  html, body { width: 801px; height: 1200px; overflow: hidden; background: var(--paper); }
  body { font-family: "Noto Sans JP", sans-serif; color: var(--ink); }

  .envelope { position: relative; width: 801px; height: 1200px; background: var(--paper); overflow: hidden; }

  .interior-backdrop {
    position: absolute; left: 0; right: 0; top: 700px; height: 390px;
    background:
      linear-gradient(90deg, rgba(255,255,255,0) 55%, rgba(190,170,140,.25) 80%, rgba(255,255,255,0) 100%),
      linear-gradient(180deg, var(--wash-top) 0%, #f4ede2 35%, var(--wash-warm) 70%, var(--wash-deep) 100%);
  }

  .branches { position: absolute; inset: 0; }

  .property-photo {
    position: absolute; border-radius: 50%;
    border: 3px solid var(--frame);
    box-shadow: 0 3px 9px rgba(0,0,0,.28);
  }
  .photo-house   { left: 336px; top: 348px; width: 118px; height: 118px;
    background: linear-gradient(160deg, #b9b4a6 0%, #7d776a 40%, #4a4438 70%, #6b624f 100%); }
  .photo-lattice { left: 526px; top: 335px; width: 134px; height: 134px;
    background: radial-gradient(circle at 45% 40%, #f0d6ac 0%, #d6a872 55%, #a87642 100%); }
  .photo-stair   { left: 181px; top: 525px; width: 118px; height: 118px;
    background: linear-gradient(135deg, #f6ecd9 0%, #e0c9a2 45%, #b08d5f 100%); }
  .photo-room    { left: 539px; top: 643px; width: 118px; height: 118px;
    background: linear-gradient(180deg, #efe4d0 0%, #c9b08a 50%, #7d6447 100%); }
  .photo-night   { left: 256px; top: 704px; width: 108px; height: 108px;
    background: radial-gradient(circle at 50% 62%, #f0b054 0%, #b86b24 35%, #3a2414 75%, #1c120b 100%); }

  .mascot {
    position: absolute; left: 470px; top: 845px; width: 180px; height: 230px;
    border-radius: 46% 46% 34% 34%;
    background: linear-gradient(180deg, #f6e46a 0%, #f2cc3e 50%, #ef9a34 100%);
    box-shadow: 0 4px 10px rgba(0,0,0,.15);
  }

  .company-block { position: absolute; left: 105px; top: 862px; }
  .brand-mark { display: flex; align-items: center; gap: 8px; }
  .brand-mark .square { width: 22px; height: 22px; background: var(--brand-red); }
  .brand-mark .brand-name { font-size: 16px; font-weight: 900; color: var(--brand-red); letter-spacing: .06em; }
  .company-name { margin-top: 44px; font-size: 19px; font-weight: 900; letter-spacing: .02em; }
  .contact { margin-top: 8px; font-size: 11px; line-height: 15.5px; font-style: normal; }
  .contact .indent { padding-left: 37px; }

  .site-band {
    position: absolute; left: 0; right: 0; top: 1085px; height: 42px;
    background: var(--band-brown);
    display: flex; align-items: center; justify-content: center;
  }
  .site-band .url { color: var(--band-text); font-size: 15px; letter-spacing: .04em; padding-left: 160px; }
</style>
</head>
<body>
<main class="envelope">
  <div class="interior-backdrop" role="img" aria-label="施工物件の室内写真を淡く加工した背景"></div>

  <svg class="branches" width="801" height="1200" viewBox="0 0 801 1200" aria-hidden="true">
    <g stroke="var(--branch)" stroke-width="1.6" fill="none" stroke-linecap="round">
      <line x1="520" y1="950" x2="395" y2="407"/>
      <line x1="441" y1="605" x2="593" y2="402"/>
      <line x1="449" y1="640" x2="240" y2="584"/>
      <line x1="482" y1="785" x2="598" y2="702"/>
      <line x1="482" y1="785" x2="310" y2="758"/>
    </g>
  </svg>

  <div class="property-photo photo-house" role="img" aria-label="施工物件の外観写真"></div>
  <div class="property-photo photo-lattice" role="img" aria-label="格子窓のディテール写真"></div>
  <div class="property-photo photo-stair" role="img" aria-label="木製階段の室内写真"></div>
  <div class="property-photo photo-room" role="img" aria-label="和室の内観写真"></div>
  <div class="property-photo photo-night" role="img" aria-label="夜の店舗外観写真"></div>

  <div class="mascot" role="img" aria-label="イメージキャラクター ヒノリくんのイラスト"></div>

  <section class="company-block">
    <div class="brand-mark"><span class="square"></span><span class="brand-name">HINORISA</span></div>
    <h1 class="company-name">株式会社 ヒノリサコーポレーション</h1>
    <address class="contact">
      〒245-0623<br>
      神奈川県横浜市戸塚区下柏尾町517-4 リベルタ北園3F<br>
      TEL&nbsp;&nbsp;&nbsp;&nbsp;045-770-2914（代表）<br>
      <span class="indent">045-770-2957（工事部）</span><br>
      <span class="indent">045-770-2986（不動産部）</span><br>
      FAX&nbsp;&nbsp;&nbsp;&nbsp;045-770-2938<br>
      E-mail&nbsp;info@hinorisa-corp.com
    </address>
  </section>

  <footer class="site-band"><span class="url">www.hinorisa-corp.com</span></footer>
</main>
</body>
</html>
```